"The Steady Harbor Ledger" needs a Book Cover Design

I need a book cover design for my book titled "The Steady Harbor Ledger". The cover style needs to be consistent with my website: http://quillmarsh-tz.example. I have uploaded some samples of covers that I think are along the right path. I utilize mind-maps or bubble maps heavily as visual aids throughout the book so I want to drive home the point that I use mind-maps/links between topics, etc to be effective in my job as an effective project manager. I even uploaded a sample photo of me that might work on the cover (a log of self-help books seem to have photos of authors on the covers) but I am open.

The ultimate message of the book - How to manage yourself and manage others in order to be an effective project manager.

If you do all the things in the book and take all the advice you too can become an effective project manager. The delivery style of the content to the reader is conversational in nature - Like I am in the person's living room providing advice based on my 20 years of experience.

The book also provides many different real-world tools (mostly mind-map templates) and charts/graphs to help a project manager manage their projects. Also I provide other tips to the reader (productivity, people and email related)

```html
<!DOCTYPE html>
<html lang="en">
<head>
<meta charset="utf-8">
<title>The Steady Harbor Ledger – Book Cover</title>
<link rel="stylesheet" href="https://fonts.googleapis.com/css2?family=Oswald:wght@400;500&family=Arimo:wght@400&display=swap">
<style>
  :root {
    --page-bg: #efece6;
    --band-dark: #1b1b1b;
    --accent-green: #8cf02c;
    --headline-gray: #b9b9b9;
    --ink: #1d1d1d;
    --paper: #ffffff;
    --foot-gray: #cfcfcf;
    --art-green: #7ed321;
    --art-gray: #8a8a8a;
  }
  * { margin: 0; padding: 0; box-sizing: border-box; }
  html, body { width: 1200px; height: 1000px; overflow: hidden; }
  body { background: var(--page-bg); position: relative; font-family: "Arimo", Arial, sans-serif; }

  .cover {
    position: absolute; top: 122px; width: 498px; height: 746px;
    background: var(--paper); overflow: hidden;
    box-shadow: 0 2px 6px rgba(0,0,0,.18);
  }
  .cover--front { left: 70px; }
  .cover--back { left: 632px; }

  .cover__top {
    position: absolute; left: 0; top: 0; width: 100%; height: 186px;
    background: var(--band-dark);
    display: flex; flex-direction: column; justify-content: center; align-items: center;
  }
  .book-title {
    font-family: "Oswald", "Arial Narrow", sans-serif; font-weight: 400;
    font-size: 72px; line-height: 1.0; color: var(--paper);
    text-align: center; text-transform: uppercase; letter-spacing: -0.5px;
  }
  .book-title .accent { color: var(--accent-green); }

  .back-headline {
    font-family: "Oswald", "Arial Narrow", sans-serif; font-weight: 400;
    font-size: 35px; line-height: 1.06; color: var(--headline-gray);
    text-align: center; letter-spacing: -0.8px;
  }
  .back-headline .accent { color: var(--accent-green); }

  .cover__art {
    position: absolute; left: 0; top: 186px; width: 100%; height: 437px;
    background:
      radial-gradient(circle at 50% 50%, #ffffff 0 14%, rgba(126,211,33,.85) 22%, rgba(70,70,70,.55) 32%, rgba(126,211,33,.75) 40%, rgba(150,150,150,.5) 48%, rgba(180,235,120,.45) 56%, rgba(255,255,255,0) 66%),
      linear-gradient(#ffffff, #f1f1f1);
  }
  .cover__art--faint {
    height: 140px;
    background:
      radial-gradient(ellipse 70% 120% at 60% 0%, rgba(160,160,160,.35) 0 30%, rgba(180,235,120,.35) 45%, rgba(255,255,255,0) 70%);
  }

  .author-bio {
    position: absolute; left: 34px; top: 240px; width: 262px;
    font-size: 10.4px; line-height: 1.28; color: var(--ink);
  }
  .author-bio p + p { margin-top: 12px; }
  .author-bio .bio-wide { width: 262px; }

  .author-photo {
    position: absolute; left: 319px; top: 406px; width: 143px; height: 192px;
    background: linear-gradient(160deg, #c9cfb8 0%, #a9b7c9 55%, #8ea6cf 100%);
  }

  .cover__name {
    position: absolute; left: 0; top: 623px; width: 100%; height: 61px;
    background: var(--band-dark);
    display: flex; align-items: center; justify-content: center;
    font-family: "Oswald", "Arial Narrow", sans-serif; font-weight: 400;
    font-size: 32px; letter-spacing: 0.5px; color: var(--accent-green); text-transform: uppercase;
  }
  .cover__foot {
    position: absolute; left: 0; top: 684px; width: 100%; height: 62px;
    background: linear-gradient(var(--foot-gray), #f4f4f4);
    display: flex; flex-direction: column; align-items: center; justify-content: center;
    font-size: 14.5px; line-height: 1.3; color: var(--ink); text-align: center;
  }
</style>
</head>
<body>

  <section class="cover cover--front">
    <header class="cover__top">
      <h1 class="book-title">The <span class="accent">Steady</span><br>Harbor Ledger</h1>
    </header>
    <div class="cover__art" role="img" aria-label="Circular mind-map pattern of green, gray and white arrows swirling around a center"></div>
    <div class="cover__name">Daniel Whitcombe</div>
    <footer class="cover__foot">
      <span>Owner and Founder of</span>
      <span>Steady Harbor Consulting, LLC</span>
    </footer>
  </section>

  <section class="cover cover--back">
    <header class="cover__top">
      <h2 class="back-headline">
        Project Managers are <span class="accent">doers.</span><br>
        Project Managers <span class="accent">make things happen.</span><br>
        Project Managers <span class="accent">know things.</span>
      </h2>
    </header>
    <div class="cover__art cover__art--faint" role="img" aria-label="Faint arc of green and gray arrows continuing the front cover pattern"></div>

    <div class="author-bio">
      <p class="bio-wide">Daniel has 15 years of experience as a business analyst, project manager and business owner. Daniel has consulted for Big 4 firms, start-ups, mid-size companies and Top 500 companies. Daniel has an M.S. in Technology Management from the Larchmont Institute (2005) and is a strong advocate for the clear identification of problems, requirements and processes before the purchase and implementation of technology solutions.</p>
      <p>Project Managers are doers. Project Managers make things happen. Project Managers know things. We are some of the most valuable people in an organization. We know who is doing what and when. We know how to determine and manage organizational problems. We have process improvement suggestions. We understand how to be efficient. We have industry knowledge. We understand the different business functions within an organization. We track things. We have insight and very valuable knowledge geared to help company leaders achieve their vision through action.</p>
      <p>"I will do what it takes to make real improvements for your business. I am passionate about working on the right tasks for the right organization. Reach out for a conversation about your project management needs".</p>
    </div>

    <div class="author-photo" role="img" aria-label="Portrait photo of the author in a light blue shirt, arms crossed"></div>

    <div class="cover__name">Daniel Whitcombe</div>
    <footer class="cover__foot">
      <span>Owner and Founder of</span>
      <span>Steady Harbor Consulting, LLC</span>
    </footer>
  </section>

</body>
</html>
```